Industrial Professional Business Card Design (Vantrel Systems)

Would like professional looking business cards. Not too busy leaning towards minimal. Should have a slogan like:
"Industrial Automation and Control".

We are a tech company that programs industrial PLC computers. We also develop custom hardware solutions. Please use the logo for inspiration.

Target Market(s)

Mining, industrial, processing, automation, factory

Industry/Entity Type

Engineering

Contact Information for Business Card

Name, phone, email, website. job title.

Font styles to use
Other font styles liked:
• droid sans

Requirements
Must have
• Use colours that go well with the logo. Not too busy design.

```html
<!DOCTYPE html>
<html lang="en">
<head>
<meta charset="utf-8">
<title>Vantrel Systems – Business Card</title>
<link rel="stylesheet" href="https://fonts.googleapis.com/css2?family=Noto+Sans:wght@400;700&display=swap">
<style>
  :root {
    --navy: #1a4a70;
    --navy-text: #1d4670;
    --orange: #e8692a;
    --paper: #f4f4f4;
    --white: #ffffff;
    --stage: #e2e2e2;
    --front-tint: rgba(255, 255, 255, 0.10);
    --back-tint: rgba(196, 208, 220, 0.45);
    --back-warm: rgba(240, 214, 196, 0.35);
  }
  * { margin: 0; padding: 0; box-sizing: border-box; }
  html, body {
    width: 1200px;
    height: 960px;
    overflow: hidden;
  }
  body {
    position: relative;
    background: var(--stage);
    font-family: "Noto Sans", "Droid Sans", sans-serif;
  }
  .card {
    position: absolute;
    left: 321px;
    width: 560px;
    height: 342px;
    overflow: hidden;
  }
  .card--front {
    top: 117px;
    background: var(--navy);
  }
  .card--back {
    top: 503px;
    background: var(--paper);
  }
  .card__tint {
    position: absolute;
    border-radius: 50%;
  }
  .card--front .card__tint {
    left: 110px;
    top: -10px;
    width: 340px;
    height: 362px;
    background: radial-gradient(circle, var(--front-tint) 0%, var(--front-tint) 55%, rgba(255,255,255,0) 72%);
  }
  .card--back .card__tint {
    left: -200px;
    top: -10px;
    width: 480px;
    height: 380px;
    background: radial-gradient(circle, var(--back-tint) 0%, var(--back-tint) 50%, var(--back-warm) 62%, rgba(244,244,244,0) 74%);
  }
  .brand {
    position: absolute;
    display: flex;
    align-items: center;
    white-space: nowrap;
    font-weight: 400;
    letter-spacing: -0.5px;
  }
  .brand__dot {
    border-radius: 50%;
    background: var(--orange);
    flex: none;
  }
  .slogan {
    position: absolute;
    white-space: nowrap;
    font-weight: 400;
    letter-spacing: 1.5px;
    text-transform: uppercase;
    color: var(--orange);
  }
  .card--front .brand {
    left: 0;
    right: 0;
    top: 186px;
    justify-content: center;
    gap: 14px;
    color: var(--white);
    font-size: 42px;
    line-height: 1;
  }
  .card--front .brand__dot { width: 18px; height: 18px; }
  .card--front .slogan {
    left: 0;
    right: 0;
    top: 242px;
    text-align: center;
    font-size: 13px;
    line-height: 16px;
  }
  .card--back .brand {
    left: 280px;
    width: 240px;
    top: 112px;
    justify-content: center;
    gap: 9px;
    color: var(--navy-text);
    font-size: 27px;
    line-height: 1;
  }
  .card--back .brand__dot { width: 12px; height: 12px; }
  .card--back .slogan {
    left: 280px;
    width: 240px;
    top: 150px;
    text-align: center;
    font-size: 10px;
    line-height: 13px;
    letter-spacing: 1px;
  }
  .holder {
    position: absolute;
    left: 39px;
    top: 166px;
  }
  .holder__name {
    color: var(--navy-text);
    font-weight: 700;
    font-size: 19px;
    line-height: 24px;
  }
  .holder__role {
    color: var(--orange);
    font-size: 15px;
    line-height: 20px;
  }
  .contact {
    position: absolute;
    left: 306px;
    top: 245px;
    list-style: none;
  }
  .contact__item {
    display: flex;
    align-items: center;
    gap: 4px;
    color: var(--navy-text);
    font-size: 15px;
    line-height: 19px;
  }
  .contact__icon {
    width: 13px;
    height: 13px;
    flex: none;
    fill: var(--orange);
    stroke: var(--orange);
  }
</style>
</head>
<body>

  <section class="card card--front" aria-label="Card front">
    <div class="card__tint" role="img" aria-label="Large faint background motif area"></div>
    <div class="brand">
      <span class="brand__dot"></span>
      <span class="brand__name">Vantrel Systems</span>
    </div>
    <p class="slogan">Industrial Automation and Control</p>
  </section>

  <section class="card card--back" aria-label="Card back">
    <div class="card__tint" role="img" aria-label="Large faint background motif area"></div>
    <div class="brand">
      <span class="brand__dot"></span>
      <span class="brand__name">Vantrel Systems</span>
    </div>
    <p class="slogan">Industrial Automation and Control</p>

    <div class="holder">
      <p class="holder__name">Daniel Harper</p>
      <p class="holder__role">President</p>
    </div>

    <ul class="contact">
      <li class="contact__item">
        <svg class="contact__icon" viewBox="0 0 16 16" aria-hidden="true">
          <path stroke="none" d="M3.6 1.2l2.3 2.9-1.4 1.9c.9 2 2.6 3.7 4.6 4.6l1.9-1.4 2.9 2.3-1.4 2.6C7 14 2 9 1 4.5z"/>
        </svg>
        <span>(123) 555-0142</span>
      </li>
      <li class="contact__item">
        <svg class="contact__icon" viewBox="0 0 16 16" aria-hidden="true">
          <rect x="1.5" y="3.5" width="13" height="9" fill="none" stroke-width="1.8"/>
          <path d="M1.5 3.5L8 9l6.5-5.5" fill="none" stroke-width="1.6"/>
        </svg>
        <span>daniel@vantrelsystems.com.au</span>
      </li>
      <li class="contact__item">
        <svg class="contact__icon" viewBox="0 0 16 16" aria-hidden="true">
          <g fill="none" stroke-width="1.3">
            <circle cx="8" cy="8" r="6.3"/>
            <ellipse cx="8" cy="8" rx="2.8" ry="6.3"/>
            <path d="M1.7 8h12.6M2.8 4.8h10.4M2.8 11.2h10.4"/>
          </g>
        </svg>
        <span>www.vantrelsystems.com.au</span>
      </li>
    </ul>
  </section>

</body>
</html>
```